Modern and Vibrant Car Wash Website

In Summary: A website using our Menus for Exterior and Full Service Car Washes: Meadowlark, tidewater car wash, Vireo and Copperleaf Express Car Wash websites (link attached below are good references for the type of cartoony fun design).

I will add our flyer, and menus, and some other graphics as a visual reference. Will over time add the files (AI and SVG so you can use them).

Car wash front page should be nice and clean. I have lots of videos and photos we can use throughout the wash. Would like a video on the landing page.

Our shop section can remain blank as my POS developers will create a hyperlink to it.

Main easy to use functions should be the Car Wash services, their price and full service ones as well. Allow customers to see, book if needed etc.

Please note I have the website on PLOM.

I have attached a general pdf as well for some more info.

https://meadowlarkgleamwash.ca/
https://tidewatercarwash.ca/
https://marblecarwash.com/
https://vireowash.com/
https://plainpagebuilder.com/carwash-website-design/
https://copperleafexpresscarwash.com/

```html
<!DOCTYPE html>
<html lang="en">
<head>
<meta charset="utf-8">
<title>Glide N' Gleam — Drive Through Tunnel Car Wash</title>
<link href="https://fonts.googleapis.com/css2?family=Poppins:wght@400;500;600;700&family=Oswald:wght@700&family=Baloo+2:wght@700;800&family=Outfit:wght@600;700&family=Allura&display=swap" rel="stylesheet">
<style>
:root{
  --blue:#0b6cbf;
  --blue-dark:#0957a0;
  --yellow:#f8c617;
  --yellow-light:#fde27e;
  --sky:#d3e8f9;
  --navy:#0d1f3c;
  --cream:#fdf0c4;
  --ink:#1d1d1d;
  --body:#333;
  --white:#fff;
}
*{box-sizing:border-box;margin:0;padding:0}
html,body{width:1200px;height:4666px;overflow:hidden}
body{position:relative;font-family:'Poppins',sans-serif;color:var(--body);background:var(--white)}
.abs{position:absolute}
.btn{position:absolute;display:flex;align-items:center;justify-content:center;font-family:'Poppins',sans-serif;font-size:12px;font-weight:500;letter-spacing:.2px;border-radius:3px;text-transform:uppercase}
.btn-blue{background:var(--blue);color:var(--white)}
.btn-yellow{background:var(--yellow);color:var(--ink)}
.script{position:absolute;font-family:'Allura',cursive;color:var(--yellow);opacity:.45;font-size:76px;line-height:1;white-space:nowrap}
.section-title{position:absolute;font-family:'Baloo 2',sans-serif;font-weight:800;color:var(--blue);font-size:31px;line-height:42px;text-transform:uppercase}
.ph{position:absolute}

/* top bar */
.topbar{position:absolute;top:0;left:0;width:1200px;height:36px;background:var(--yellow-light)}
.social-dot{position:absolute;top:9px;width:18px;height:18px;border-radius:50%;background:var(--yellow)}
.topbar .btn{top:0;height:36px;border-radius:0;font-size:12px}

/* nav */
.nav{position:absolute;top:36px;left:0;width:1200px;height:96px;background:var(--white)}
.nav a{position:absolute;top:40px;font-size:12px;color:var(--ink);text-decoration:none;text-transform:uppercase;letter-spacing:.2px}
.nav a.active{color:var(--blue)}
.brand{position:absolute;font-family:'Baloo 2',sans-serif;font-weight:800;color:var(--blue);white-space:nowrap;display:flex;align-items:center;gap:8px}
.brand .mark{width:14px;height:14px;border-radius:50%;background:var(--yellow)}

/* hero */
.hero{position:absolute;top:132px;left:0;width:1200px;height:680px;background:linear-gradient(90deg,#3b3b3b 0%,#4a4a48 38%,#6f7a82 60%,#9fb3bf 80%,#c3d2da 100%)}
.hero-copy{position:absolute;left:141px;top:150px;width:500px;display:flex;flex-direction:column}
.hero h1{font-family:'Oswald',sans-serif;font-weight:700;font-size:31px;line-height:35px;color:var(--white);text-transform:uppercase}
.hero p{margin-top:14px;width:470px;font-size:15.5px;line-height:23px;color:var(--white)}
.hero-actions{display:flex;gap:8px;margin-top:20px}
.hero-actions .btn{position:static;height:35px}

/* about */
.about-text p{position:absolute;left:637px;width:420px;font-size:12.5px;line-height:24px;color:var(--body)}

/* services */
.tabs{position:absolute;top:1498px;left:389px;width:422px;height:30px;border-bottom:1px solid #d8d8d8}
.tabs span{position:absolute;top:0;font-size:13.5px;color:var(--ink);text-transform:uppercase}
.tabs span.active{color:var(--blue);border-bottom:2px solid var(--blue);padding-bottom:7px}
.service{position:absolute;top:1566px;width:220px;text-align:center}
.service .pic{width:212px;height:190px;margin:0 auto;border:2px dashed #a7b9c9;border-radius:48% 52% 44% 56% / 56% 48% 52% 44%;padding:5px}
.service .pic div{width:100%;height:100%;border-radius:48% 52% 44% 56% / 56% 48% 52% 44%}
.service h3{margin-top:20px;font-size:14.5px;font-weight:500;color:var(--ink);text-transform:uppercase}
.service p{margin-top:4px;font-size:12.5px;line-height:21px}
.service .price{margin-top:6px;font-family:'Baloo 2',sans-serif;font-weight:800;font-size:20px;color:var(--blue)}
.service .btn{position:relative;margin:8px auto 0;width:106px;height:34px;font-size:12px}

/* launch */
.launch{position:absolute;top:2010px;left:0;width:1200px;height:526px;background:var(--sky)}
.launch h2{position:absolute;top:224px;left:0;width:1200px;text-align:center;font-family:'Outfit',sans-serif;font-weight:700;font-size:45px;line-height:57px;color:var(--ink);text-transform:uppercase}
.launch p{position:absolute;top:339px;left:0;width:1200px;text-align:center;font-size:12.5px;line-height:18px}

/* why */
.why{position:absolute;top:2535px;left:0;width:1200px;height:558px;background:var(--yellow)}
.why-card{position:absolute;top:217px;width:212px;height:218px;border-radius:26px 34px 24px 30px;box-shadow:0 4px 10px rgba(0,0,0,.12);text-align:center;padding-top:28px}
.why-card.cream{background:var(--cream)}
.why-card.skyc{background:#dcecfb}
.why-card svg{display:block;margin:0 auto}
.why-card h3{margin-top:14px;font-size:14.5px;font-weight:500;color:var(--ink);text-transform:uppercase}
.why-card p{margin-top:6px;font-size:12.5px;line-height:19px;padding:0 14px}

/* testimonials */
.review{position:absolute;top:3329px;width:438px;height:242px;border:1.5px dashed #f3d77a;border-radius:28px;padding:24px 26px}
.review .avatar{position:absolute;left:26px;top:22px;width:68px;height:68px;border-radius:50%;background:linear-gradient(135deg,#c9b3a3,#7d6a5f)}
.review .name{position:absolute;left:110px;top:32px;font-size:14.5px;color:var(--ink);text-transform:uppercase}
.review .loc{position:absolute;left:110px;top:52px;font-size:10px;color:#555}
.review .stars{position:absolute;right:26px;top:30px;color:#f5a623;font-size:17px;letter-spacing:1px}
.review p{position:absolute;left:26px;top:100px;width:390px;font-size:12.5px;line-height:24px}
.review .quote{position:absolute;right:38px;bottom:-36px;font-family:'Baloo 2',sans-serif;font-weight:800;font-size:96px;line-height:1;color:var(--yellow)}
.dot{position:absolute;top:3606px;width:14px;height:14px;border-radius:50%;background:#a8cdee}
.dot.on{background:var(--blue)}

/* signup */
.signup{position:absolute;top:3722px;left:0;width:1200px;height:560px;background:linear-gradient(180deg,#0b63b0 0%,#0c6cbf 60%,#0e74c8 100%)}
.field{position:absolute;height:32px;background:var(--white);border-radius:2px;font-size:10.5px;color:#333;padding-left:14px;display:flex;align-items:center}
.check{position:absolute;top:4094px;display:flex;align-items:center;gap:8px;font-size:10.5px;color:var(--white)}
.check i{display:block;width:15px;height:15px;border:1.5px solid var(--white);border-radius:2px}

/* footer */
.footer{position:absolute;top:4220px;left:0;width:1200px;height:446px;background:var(--navy);color:#dfe6f1}
.footer h4{position:absolute;font-size:13.5px;font-weight:600;color:var(--white);text-transform:uppercase}
.footer .links a{position:absolute;left:431px;font-size:12.5px;color:#dfe6f1;text-decoration:none}
.footer .contact{position:absolute;left:600px;display:flex;gap:12px;font-size:12px;line-height:18px}
.footer .hours div{position:absolute;left:874px;font-size:12px;white-space:pre}
.fsocial{position:absolute;top:4518px;width:32px;height:32px;border-radius:50%;border:1.5px solid #dfe6f1}
</style>
</head>
<body>

<!-- top bar -->
<div class="topbar">
  <span class="social-dot" style="left:143px"></span>
  <span class="social-dot" style="left:168px"></span>
  <span class="social-dot" style="left:193px"></span>
  <span class="social-dot" style="left:218px"></span>
  <span class="btn btn-yellow" style="left:748px;width:150px">Book Appointment</span>
  <span class="btn btn-blue" style="left:906px;width:152px">Save on every wash</span>
</div>

<!-- nav -->
<nav class="nav">
  <a class="active" style="left:221px">Home</a>
  <a style="left:300px">About Us</a>
  <a style="left:405px">Services</a>
  <div class="brand" style="left:508px;top:30px;font-size:22px"><span class="mark"></span>GLIDE N' GLEAM</div>
  <a style="left:727px">Pricing</a>
  <a style="left:820px">Wash Cards</a>
  <a style="left:948px">Contact Us</a>
</nav>

<!-- hero -->
<section class="hero">
  <div class="ph" role="img" aria-label="Car driving through the tunnel wash with blue brushes and water spray" style="left:560px;top:0;width:640px;height:560px;background:radial-gradient(ellipse at 60% 45%,#d9e3e8 0%,#9fb0bb 45%,rgba(90,100,108,0) 80%)"></div>
  <div class="hero-copy">
    <h1>Alder Creek's First State of the Art Drive Through Tunnel Car Wash</h1>
    <p>Experience the ultimate car care with our professional washing services. From quick exterior washes to full-service detailing, we make your car shine like new!</p>
    <div class="hero-actions">
      <span class="btn btn-yellow" style="width:152px">Book Appointment</span>
      <span class="btn btn-blue" style="width:160px">Save on every wash</span>
    </div>
  </div>
  <svg class="abs" style="left:0;top:468px" width="1200" height="214" viewBox="0 0 1200 214" aria-hidden="true">
    <path d="M0 158 C320 90 720 20 1200 8 L1200 214 L0 214 Z" fill="var(--blue)"/>
    <path d="M0 208 C330 120 720 40 1200 22 L1200 214 L0 214 Z" fill="#fff"/>
  </svg>
</section>

<!-- about -->
<section class="about">
  <div class="ph" role="img" aria-label="Cartoon car on a skateboard with a tow line" style="left:986px;top:716px;width:100px;height:80px;border-radius:16px;background:linear-gradient(135deg,#7cc3ea,#e2473c)"></div>
  <div class="ph" style="left:141px;top:815px;width:430px;height:378px;border:2px dashed #a7b9c9;border-radius:46% 54% 40% 60% / 58% 44% 56% 42%;padding:6px">
    <div role="img" aria-label="Car wash building exterior with tunnel entrance and a car parked in front" style="width:100%;height:100%;border-radius:46% 54% 40% 60% / 58% 44% 56% 42%;background:linear-gradient(160deg,#5d7387 0%,#c8ced4 45%,#8c8f94 75%,#4f555c 100%)"></div>
  </div>
  <div class="ph" role="img" aria-label="Cartoon car with soap bubbles" style="left:200px;top:1100px;width:150px;height:90px;border-radius:40px;background:linear-gradient(135deg,#5bc0f0,#f6c945)"></div>
  <div class="ph" role="img" aria-label="Cartoon spray nozzle" style="left:456px;top:876px;width:70px;height:70px;border-radius:50%;background:linear-gradient(135deg,#e53b3b,#fbd6d6)"></div>

  <div class="script" style="left:637px;top:752px">Car Clean</div>
  <h2 class="section-title" style="left:637px;top:820px;width:440px">Keeping your car clean<br>is easy and affordable</h2>
  <div class="about-text">
    <p style="top:918px">Lorem ipsum dolor sit amet, consectetuer adipiscing elit, sed diam nonummy nibh euismod tincidunt ut laoreet dolore magna aliquam erat volutpat. Ut wisi enim ad minim veniam, quis nostrud exerci tation ullamcorper suscipit lobortis nisl ut aliquip ex ea commodo consequat.</p>
    <p style="top:1042px">Duis autem vel eum iriure dolor in hendrerit in vulputate velit esse molestie consequat, vel illum dolore eu feugiat nulla facilisis at vero eros et accumsan et iusto odio dignissim qui blandit.</p>
  </div>
  <span class="btn btn-blue" style="left:637px;top:1142px;width:107px;height:34px">Read More</span>
</section>

<!-- services -->
<section class="services">
  <div class="script" style="left:430px;top:1250px">Our Services</div>
  <h2 class="section-title" style="left:0;top:1318px;width:1200px;text-align:center">Better wash features,<br>brighter clean</h2>
  <p class="abs" style="left:0;top:1420px;width:1200px;text-align:center;font-size:12.5px;line-height:24px">Lorem ipsum dolor sit amet, consectetuer adipiscing elit, sed diam nonummy nibh<br>euismod tincidunt ut laoreet dolore magna aliquam erat volutpat.</p>
  <div class="tabs">
    <span class="active" style="left:0">Exterior Wash</span>
    <span style="left:164px">Wash Books</span>
    <span style="left:316px">Full Services</span>
  </div>

  <div class="service" style="left:138px">
    <div class="pic"><div role="img" aria-label="Gloved hand polishing a red car with a buffer pad" style="background:linear-gradient(150deg,#2d2d2d 0%,#8a1d22 55%,#e14a4a 100%)"></div></div>
    <h3>Ultimate Ceramic Shine</h3>
    <p>Lorem ipsum dolor sit amet,<br>consectetuer adipiscing elit</p>
    <div class="price">$25.99</div>
    <span class="btn btn-blue">Read More</span>
  </div>
  <div class="service" style="left:372px">
    <div class="pic"><div role="img" aria-label="Black sports car covered in foam under blue light" style="background:linear-gradient(150deg,#1d3652 0%,#5e86a8 55%,#16283c 100%)"></div></div>
    <h3>Signature Shine</h3>
    <p>Lorem ipsum dolor sit amet,<br>consectetuer adipiscing elit</p>
    <div class="price">$17.99</div>
    <span class="btn btn-yellow">Read More</span>
  </div>
  <div class="service" style="left:607px">
    <div class="pic"><div role="img" aria-label="Worker washing a purple car with a pressure hose" style="background:linear-gradient(150deg,#3a3f4a 0%,#5b3f6e 55%,#262a33 100%)"></div></div>
    <h3>Pro Shine</h3>
    <p>Lorem ipsum dolor sit amet,<br>consectetuer adipiscing elit</p>
    <div class="price">$13.99</div>
    <span class="btn btn-yellow">Read More</span>
  </div>
  <div class="service" style="left:842px">
    <div class="pic"><div role="img" aria-label="Dark sedan in a wash bay with water spray" style="background:linear-gradient(150deg,#203a5a 0%,#4f7aa3 55%,#14233a 100%)"></div></div>
    <h3>Value Shine</h3>
    <p>Lorem ipsum dolor sit amet,<br>consectetuer adipiscing elit</p>
    <div class="price">$10.99</div>
    <span class="btn btn-yellow">Read More</span>
  </div>
  <div class="ph" role="img" aria-label="Cartoon orange bucket of soap with a spray nozzle" style="left:1102px;top:1740px;width:88px;height:170px;border-radius:20px;background:linear-gradient(180deg,#e9f4fb 0%,#f5b731 55%,#ee8a1f 100%)"></div>
  <span class="btn btn-blue" style="left:512px;top:1964px;width:176px;height:34px">View full wash menu</span>
</section>

<!-- launch -->
<section class="launch">
  <svg class="abs" style="left:0;top:0" width="1200" height="120" viewBox="0 0 1200 120" aria-hidden="true">
    <path d="M0 0 H1200 V0 C860 150 360 130 0 18 Z" fill="#fff"/>
    <path d="M0 18 C360 130 860 150 1200 0" fill="none" stroke="var(--blue)" stroke-width="14"/>
  </svg>
  <h2>Launch your car wash Glide<br>N' Gleam to new heights</h2>
  <p>Lorem ipsum dolor sit amet, consectetuer adipiscing elit, sed diam nonummy nibh<br>euismod tincidunt ut laoreet dolore magna aliquam erat volutpat.</p>
  <span class="btn btn-blue" style="left:522px;top:406px;width:156px;height:34px">Book Appointment</span>
</section>

<!-- why -->
<section class="why">
  <div class="script" style="left:390px;top:96px;color:#fff;opacity:.4">Why Choose Us</div>
  <h2 class="section-title" style="left:0;top:150px;width:1200px;text-align:center">Why go unlimited?</h2>

  <div class="why-card cream" style="left:141px">
    <svg width="44" height="44" viewBox="0 0 44 44" fill="none" stroke="var(--blue)" stroke-width="2"><circle cx="24" cy="16" r="11"/><path d="M24 10v12M21 13h5a2 2 0 010 4h-4a2 2 0 000 4h5"/><path d="M4 34c5-4 10-5 16-2h8c2 0 2 3 0 3h-8M4 40c6-2 12-1 18 0 4 1 10-4 14-8"/></svg>
    <h3>Great Value</h3>
    <p>Lorem ipsum dolor sit amet, consectetuer adipiscing elit, sed diam nonummy nibh</p>
  </div>
  <div class="why-card skyc" style="left:376px">
    <svg width="44" height="44" viewBox="0 0 44 44" fill="none" stroke="var(--blue)" stroke-width="2"><circle cx="22" cy="10" r="6"/><path d="M22 7v6"/><path d="M8 26c0-6 6-10 14-10s14 4 14 10-6 10-14 10S8 32 8 26z"/><path d="M14 35v4M30 35v4M36 24h4"/></svg>
    <h3>Save Money</h3>
    <p>Lorem ipsum dolor sit amet, consectetuer adipiscing elit, sed diam nonummy nibh</p>
  </div>
  <div class="why-card cream" style="left:614px">
    <svg width="44" height="44" viewBox="0 0 44 44" fill="none" stroke="var(--blue)" stroke-width="2"><circle cx="22" cy="22" r="16"/><circle cx="22" cy="22" r="11"/><path d="M22 15v7l5 3"/></svg>
    <h3>Convenient</h3>
    <p>Lorem ipsum dolor sit amet, consectetuer adipiscing elit, sed diam nonummy nibh</p>
  </div>
  <div class="why-card skyc" style="left:848px">
    <svg width="44" height="44" viewBox="0 0 44 44" fill="none" stroke="var(--blue)" stroke-width="2"><circle cx="12" cy="20" r="4"/><circle cx="22" cy="18" r="4"/><circle cx="32" cy="20" r="4"/><path d="M4 36c0-5 4-8 8-8s8 3 8 8M14 36c0-6 4-10 8-10s8 4 8 10M24 36c0-5 4-8 8-8s8 3 8 8"/><path d="M10 8l2 3M22 5v4M34 8l-2 3"/></svg>
    <h3>Happy &amp; Cleaner</h3>
    <p>Lorem ipsum dolor sit amet, consectetuer adipiscing elit, sed diam nonummy nibh</p>
  </div>
</section>

<!-- testimonials -->
<section class="reviews">
  <div class="script" style="left:372px;top:3178px">Happy Customers</div>
  <h2 class="section-title" style="left:0;top:3228px;width:1200px;text-align:center">Why customers love us</h2>
  <svg class="abs" style="left:106px;top:3440px" width="28" height="20" viewBox="0 0 28 20" fill="none" stroke="#5aa3dc" stroke-width="3"><path d="M26 10H3M11 2L3 10l8 8"/></svg>
  <svg class="abs" style="left:1066px;top:3440px" width="28" height="20" viewBox="0 0 28 20" fill="none" stroke="var(--blue)" stroke-width="3"><path d="M2 10h23M17 2l8 8-8 8"/></svg>

  <div class="review" style="left:141px">
    <div class="avatar" role="img" aria-label="Customer portrait"></div>
    <div class="name">Dana R.</div>
    <div class="loc">Alder Creek, ON</div>
    <div class="stars">★★★★★</div>
    <p>Lorem ipsum dolor sit amet, consectetuer adipiscing elit, sed diam nonummy nibh euismod tincidunt ut laoreet dolore magna aliquam erat volutpat. Ut wisi enim ad minim veniam, quis nostrud exerci tation ullamcorper suscipit lobo.</p>
    <div class="quote">”</div>
  </div>
  <div class="review" style="left:621px">
    <div class="avatar" role="img" aria-label="Customer portrait"></div>
    <div class="name">Miles T.</div>
    <div class="loc">Alder Creek, ON</div>
    <div class="stars">★★★★★</div>
    <p>Lorem ipsum dolor sit amet, consectetuer adipiscing elit, sed diam nonummy nibh euismod tincidunt ut laoreet dolore magna aliquam erat volutpat. Ut wisi enim ad minim veniam, quis nostrud exerci tation ullamcorper suscipit lobo.</p>
    <div class="quote">”</div>
  </div>

  <span class="dot" style="left:552px"></span>
  <span class="dot" style="left:572px"></span>
  <span class="dot on" style="left:593px"></span>
  <span class="dot" style="left:614px"></span>
  <span class="dot" style="left:634px"></span>
</section>

<!-- footer base (behind signup wave) -->
<footer class="footer">
  <div class="brand" style="left:141px;top:168px;font-size:24px;color:var(--white)"><span class="mark"></span>GLIDE N' GLEAM</div>
  <p class="abs" style="left:141px;top:262px;width:230px;font-size:12.5px;line-height:19px">Lorem ipsum dolor sit amet, consectetuer adipiscing elit, sed diam nonummy nibh euismod tincidunt ut laoreet dolore magna</p>

  <h4 style="left:431px;top:168px">Quick Links</h4>
  <div class="links">
    <a style="top:208px">Home</a>
    <a style="top:231px">About Us</a>
    <a style="top:254px">Services</a>
    <a style="top:277px">Pricing</a>
    <a style="top:300px">Wash Cards</a>
    <a style="top:323px">Contact Us</a>
  </div>

  <h4 style="left:600px;top:168px">Contact Details</h4>
  <div class="contact" style="top:206px">
    <svg width="26" height="30" viewBox="0 0 26 30" fill="none" stroke="#dfe6f1" stroke-width="1.6"><path d="M13 28s9-9 9-16a9 9 0 00-18 0c0 7 9 16 9 16z"/><circle cx="13" cy="12" r="3.5"/></svg>
    <div>480 Fernway Rd<br>Alder Creek, ON K0A 2Z9</div>
  </div>
  <div class="contact" style="top:256px">
    <svg width="26" height="30" viewBox="0 0 26 30" fill="none" stroke="#dfe6f1" stroke-width="1.6"><path d="M6 4l5 1 2 6-3 2c1 3 4 6 7 7l2-3 6 2 1 5c-1 2-3 3-5 3C11 27 3 19 3 9c0-2 1-4 3-5z"/></svg>
    <div>PHONE<br>555-014-2287</div>
  </div>
  <div class="contact" style="top:304px">
    <svg width="26" height="30" viewBox="0 0 26 30" fill="none" stroke="#dfe6f1" stroke-width="1.6"><rect x="2" y="8" width="22" height="16" rx="1"/><path d="M2 9l11 8 11-8"/></svg>
    <div>EMAIL<br>hello@glidengleam.ca</div>
  </div>

  <h4 style="left:874px;top:168px">Opening Hours</h4>
  <div class="hours">
    <div style="top:210px">Mon - Fri      :    9.00 to 6.30</div>
    <div style="top:236px">Saturday      :    10.30 to 5.30</div>
    <div style="top:262px">Sunday         :    10.30 to 2.30</div>
  </div>
  <span class="fsocial" style="left:874px;top:298px"></span>
  <span class="fsocial" style="left:913px;top:298px"></span>
  <span class="fsocial" style="left:952px;top:298px"></span>
  <span class="fsocial" style="left:991px;top:298px"></span>

  <div class="abs" style="left:141px;top:380px;width:918px;height:1px;background:#34466a"></div>
  <p class="abs" style="left:0;top:404px;width:1200px;text-align:center;font-size:12px">© 2025 Glide N' Gleam. All Rights Reserved.</p>
</footer>

<!-- signup -->
<section class="signup">
  <div class="ph" role="img" aria-label="Car wash building with cars in the lot, tinted blue" style="left:0;top:40px;width:1200px;height:470px;background:radial-gradient(ellipse at 50% 40%,rgba(255,255,255,.12),rgba(255,255,255,0) 70%)"></div>
  <div class="script" style="left:450px;top:86px;color:#fff;opacity:.25">Free Wash</div>
  <h2 class="section-title" style="left:0;top:140px;width:1200px;text-align:center;color:var(--white)">Sign up today for a<br>free car wash!</h2>
  <div class="ph" role="img" aria-label="Cartoon spray nozzle with water" style="left:852px;top:184px;width:96px;height:90px;border-radius:50%;background:linear-gradient(135deg,#e53b3b,#dbeefa)"></div>
  <div class="ph" role="img" aria-label="Cartoon car in soap bubbles" style="left:188px;top:400px;width:150px;height:110px;border-radius:40px;background:linear-gradient(135deg,#5bc0f0,#f6c945)"></div>
  <svg class="abs" style="left:0;top:440px" width="1200" height="120" viewBox="0 0 1200 120" aria-hidden="true">
    <path d="M0 28 C360 110 820 110 1200 30 L1200 120 L0 120 Z" fill="var(--navy)"/>
    <path d="M0 28 C360 110 820 110 1200 30" fill="none" stroke="var(--yellow)" stroke-width="14"/>
  </svg>
</section>
<div class="field" style="left:311px;top:3957px;width:282px">First name*</div>
<div class="field" style="left:608px;top:3957px;width:282px">Last name*</div>
<div class="field" style="left:311px;top:4004px;width:282px">Phone*</div>
<div class="field" style="left:608px;top:4004px;width:282px">Email*</div>
<div class="field" style="left:311px;top:4053px;width:579px">Postal Code*</div>
<div class="check" style="left:346px"><i></i>Sign up to receive Exclusive Offers, News and More!</div>
<div class="check" style="left:670px"><i></i>CLAIM YOUR FREE CAR WASH!</div>
<span class="btn btn-yellow" style="left:460px;top:4128px;width:281px;height:33px;font-weight:600;font-size:13px">Submit Now</span>

</body>
</html>
```